Stationary for Beauty and Spa School

Create a business card, letterhead and envelopes (primarily #10 envelope with and without window and catalog envelope) for a beauty and wellness school in Miami, Fl. We offer 8 different programs of study and need an eye catching look. Looking for a combination of modern yet sophisticated. Nothing corporate or business looking. Would like to have a look and feel that is similar (or incorporates aspects) of a new website we will be launching in the next 30 days (screen shot attached.)

The final design should communicate style and elegance in a down to earth and friendly way. We strive to provide our students with quality education, friendly and amicable staff and experienced instructors.
Updates

Hello. FYI, in order to print an aesthetically appealing business card, we would like to print them (the business cards) using silk printing method, with spot UV coating (on some elements, maybe the logo, or depending on the design) and die cuts. Please think of this when preparing your design.

Only 1 day left, please submit your designs for selection. Thanks

Target Market(s)

Adults 18-49 years who are mostly interested in beauty and fashion. Need a youthful & modern look, yet sophisticated and elegant.

Industry/Entity Type

School

Colors
e34197
6b449b
add136
f79021

Requirements
Must have
• Similar look and feel as website (see attached screen shot)
Same look and feel of website (see attached screenshot)
Logo
Address: 5216 SW 3rd Avenue. Miami, Fl 33155
Telephone: 305-514-9382
Fax: 786-420-5163
website/url: www.luminora.edu
incorporate Photo of blonde model (attached)
Nice to have
• Tag line: "Beautify your future." Also, maybe two-sided business card. Would be nice if we could mention our programs (maybe in the back of the card). Below are the program offerings (names cannot be changed but order is irrelevant)... Cosmetology, Barber, Spa Therapy, Massage Therapy, Makeup Artistry, Skin Care, Manicure, Pedicure & Nail Extensions, Full Specialist.

A design with text plus a beautiful photo of a model is appealing. Attached to the files is a sample of a cover for a student handbook we have created. You should use the photo of the blonde model (attached) in your design. The original (quality) version of this stock photograph has been uploaded.

Also would be nice to request clients to follow us on facebook and instagram by including the icons.
Should not have
• A corporate or business look. We are a vocational school teaching beauty and spa programs and we like our advertising to have a look that resembles the industry. We do not want a very serious look or snobby feel.

```html
<!DOCTYPE html>
<html lang="en">
<head>
<meta charset="utf-8">
<title>Luminora School of Beauty – Business Card</title>
<link rel="stylesheet" href="https://fonts.googleapis.com/css2?family=Arimo:wght@400&display=swap">
<style>
  :root {
    --page-bg: #f2f2f2;
    --card-black: #000000;
    --card-white: #ffffff;
    --ink-light: #ffffff;
    --ink-dark: #111111;
    --card-shadow: rgba(0, 0, 0, 0.18);
  }
  html, body {
    margin: 0;
    padding: 0;
    width: 1200px;
    height: 682px;
    overflow: hidden;
    background: var(--page-bg);
  }
  .board {
    position: relative;
    width: 1200px;
    height: 682px;
  }
  .card {
    position: absolute;
    left: 332px;
    width: 536px;
    box-shadow: 0 1px 4px var(--card-shadow);
  }
  .card--front { top: 30px; height: 296px; }
  .card--back  { top: 354px; height: 298px; }
  .card svg { display: block; width: 100%; height: 100%; }
  .card text {
    font-family: "Arimo", Arial, sans-serif;
  }
  .contact { fill: var(--ink-light); font-size: 14px; }
  .tagline { fill: var(--ink-light); font-size: 17.5px; }
  .web { fill: var(--ink-light); font-size: 17.5px; letter-spacing: 4.2px; }
  .brand-name { fill: var(--ink-dark); font-size: 72px; }
  .brand-sub { fill: var(--ink-dark); font-size: 17px; letter-spacing: 0.4px; }
  .programs { fill: var(--ink-light); font-size: 17.5px; }
  .bg-black { fill: var(--card-black); }
  .bg-white { fill: var(--card-white); }
</style>
</head>
<body>
<main class="board">

  <!-- Card front: contact side -->
  <section class="card card--front">
    <svg viewBox="0 0 536 296" xmlns="http://www.w3.org/2000/svg">
      <defs>
        <radialGradient id="flourishFront" cx="50%" cy="50%" r="50%">
          <stop offset="0%" stop-color="#7a7a7a" stop-opacity="0.35"/>
          <stop offset="100%" stop-color="#7a7a7a" stop-opacity="0"/>
        </radialGradient>
      </defs>
      <rect class="bg-black" width="536" height="296"/>
      <ellipse role="img" aria-label="Decorative grey swirl flourishes" cx="170" cy="200" rx="170" ry="90" fill="url(#flourishFront)"/>
      <path class="bg-white" d="M0,296 C140,268 240,160 320,108 C395,62 465,48 536,46 L536,296 Z"/>
      <text class="contact" x="14" y="23">Address: 5216 SW 3rd Avenue. Miami, Fl 33155</text>
      <text class="contact" x="518" y="18" text-anchor="end">T. 305-514-9382</text>
      <text class="contact" x="518" y="37" text-anchor="end">F. 786-420-5163</text>
      <text class="tagline" x="176" y="108" text-anchor="middle">"Beautify your future."</text>
      <text class="web" x="12" y="137">www.luminora.edu</text>
      <text class="brand-name" x="212" y="258">Luminora</text>
      <text class="brand-sub" x="290" y="283">SCHOOL OF BEAUTY</text>
    </svg>
  </section>

  <!-- Card back: programs side -->
  <section class="card card--back">
    <svg viewBox="0 0 536 298" xmlns="http://www.w3.org/2000/svg">
      <defs>
        <radialGradient id="flourishBack" cx="50%" cy="50%" r="50%">
          <stop offset="0%" stop-color="#7a7a7a" stop-opacity="0.35"/>
          <stop offset="100%" stop-color="#7a7a7a" stop-opacity="0"/>
        </radialGradient>
      </defs>
      <rect class="bg-white" width="536" height="298"/>
      <path class="bg-black" d="M0,298 L0,282 C120,256 230,160 310,110 C385,60 460,14 536,0 L536,298 Z"/>
      <ellipse role="img" aria-label="Decorative grey swirl flourishes along the curve" cx="300" cy="175" rx="200" ry="80" fill="url(#flourishBack)"/>
      <text class="brand-name" x="10" y="86">Luminora</text>
      <text class="brand-sub" x="88" y="114">SCHOOL OF BEAUTY</text>
      <g class="programs" text-anchor="end">
        <text x="520" y="102">Cosmetology</text>
        <text x="520" y="124.5">Barber</text>
        <text x="520" y="147">Spa Therapy</text>
        <text x="520" y="169.5">Massage Therapy</text>
        <text x="520" y="192">Makeup Artistry</text>
        <text x="520" y="214.5">Skin Care</text>
        <text x="520" y="237">Manicure</text>
        <text x="520" y="259.5">Pedicure &amp; Nail Extensions</text>
        <text x="520" y="282">Full Specialist</text>
      </g>
    </svg>
  </section>

</main>
</body>
</html>
```